Chairside Roots: the dental helper's field guide, start to finish

Book cover:

Book about dental implantology
Reader is a dental assistant
Introduction to surgical knowledge to case acceptance. We will start with the intro to implants that will cover population stats on tooth loss, how to make the patient trust the team, how to communicate with the patient. Then we will get more technical; bone loss, bone quality and quantity. We will also inform on pros and cons of different classic dental treatments vs implant treatment. Surgical knowledge deep into various aspects of implants procedures. An illustration of surgical instruments needed and motors and hand pieces. Operatory set up will be demonstrated. I’ll be guiding the role of the surgical assistant and non surgical assistant. At the end I’ll explain how to close an implant case. From single implants to more complex cases.

Target Market(s)

Dental assistants

Industry/Entity Type

Dental

Font styles to use
Other font styles liked:
• Mellifluous or addington

Colors
EE7325
F08F49
F5BC92
FAE3D3
FDF4ED

Requirements
Must have
• Dental implant, positive vibe, orange Colors, professional
Nice to have
• Sense of team spirit, uncluttered,
Should not have
• Images of people

```html
<!DOCTYPE html>
<html lang="en">
<head>
<meta charset="utf-8">
<title>Chairside Roots – Book Cover</title>
<link href="https://fonts.googleapis.com/css2?family=Bebas+Neue&family=Montserrat:wght@500;600&family=Chewy&display=swap" rel="stylesheet">
<style>
  :root {
    --bg-edge: #f29214;
    --bg-mid: #f7a934;
    --bg-glow: #fcc556;
    --blob-light: #fb9c3a;
    --blob-deep: #fa7b0b;
    --ink: #0b0b0b;
    --paper: #ffffff;
    --metal-light: #f4f4f4;
    --metal-dark: #9a9a9a;
  }
  * { margin: 0; padding: 0; box-sizing: border-box; }
  html, body {
    width: 849px; height: 1200px; overflow: hidden; background: var(--bg-edge);
  }
  .cover {
    position: relative; width: 849px; height: 1200px; overflow: hidden;
    background:
      linear-gradient(to bottom, transparent 0, transparent 1010px, rgba(252,197,86,0.55) 1075px, transparent 1200px),
      radial-gradient(ellipse 520px 560px at 411px 560px, var(--bg-glow) 0%, var(--bg-mid) 55%, var(--bg-edge) 100%);
  }
  .art { position: absolute; inset: 0; }
  .title {
    position: absolute; top: 129px; left: 0; width: 100%;
    text-align: center; font-family: "Bebas Neue", "Arial Narrow", sans-serif;
    font-size: 146px; line-height: 119px; color: var(--ink); letter-spacing: 1px;
  }
  .subtitle {
    position: absolute; top: 380px; left: 0; width: 100%; text-align: center;
    font-family: "Montserrat", sans-serif; font-weight: 500; font-size: 25px;
    letter-spacing: 0.1em; color: var(--paper);
  }
  .range-pill {
    position: absolute; top: 429px; left: 289px; width: 252px; height: 50px;
    border: 1.3px solid #2a2a2a; border-radius: 25px;
    display: flex; align-items: center; justify-content: center; gap: 10px;
    font-family: "Montserrat", sans-serif; font-weight: 600; font-size: 22px; color: var(--ink);
  }
  .range-arrow { width: 52px; height: 10px; }
  .blob-label {
    position: absolute; font-family: "Chewy", cursive; font-size: 22px;
    line-height: 24px; color: var(--ink);
  }
  .label-efficiency { left: 242px; top: 612px; }
  .label-matters { left: 563px; top: 700px; }
  .label-takes { left: 216px; top: 843px; }
  .label-team { left: 492px; top: 905px; }
  .author {
    position: absolute; top: 1078px; left: 0; width: 100%; text-align: center;
    font-family: "Montserrat", sans-serif; font-weight: 500; font-size: 19px;
    letter-spacing: 0.95em; padding-left: 0.95em; color: var(--ink);
  }
</style>
</head>
<body>
<div class="cover">
  <svg class="art" width="849" height="1200" viewBox="0 0 849 1200">
    <defs>
      <linearGradient id="implantTone" x1="0" y1="0" x2="0" y2="1">
        <stop offset="0" stop-color="var(--metal-light)"/>
        <stop offset="0.45" stop-color="#e2e2e2"/>
        <stop offset="1" stop-color="var(--metal-dark)"/>
      </linearGradient>
    </defs>
    <circle class="orbit" cx="413" cy="785" r="175" fill="none" stroke="#ffffff" stroke-width="1.2"/>
    <path class="blob blob-efficiency" fill="var(--blob-light)"
      d="M250 590 C290 565 330 580 355 620 C375 650 372 680 340 695 C300 712 260 710 240 690 C220 665 205 620 250 590 Z"/>
    <rect class="implant-visual" role="img" aria-label="Dental implant: white crown on a titanium screw"
      x="288" y="519" width="236" height="497" rx="44" fill="url(#implantTone)"/>
    <path class="blob blob-matters" fill="var(--blob-light)"
      d="M575 675 C610 660 650 648 662 680 C672 720 668 760 640 770 C600 778 545 770 520 745 C505 725 515 695 575 675 Z"/>
    <path class="blob blob-takes" fill="var(--blob-deep)"
      d="M240 802 C285 798 315 815 308 860 C300 895 285 918 255 920 C215 922 175 905 171 875 C168 840 200 806 240 802 Z"/>
    <path class="blob blob-team" fill="var(--blob-deep)"
      d="M520 870 C560 872 600 910 608 945 C612 975 570 995 535 1000 C495 1004 470 985 462 955 C455 920 470 868 520 870 Z"/>
  </svg>

  <h1 class="title">CHAIRSIDE<br>ROOTS</h1>
  <p class="subtitle">THE DENTAL HELPER'S FIELD GUIDE</p>
  <div class="range-pill">
    <span>start</span>
    <svg class="range-arrow" viewBox="0 0 52 10"><line x1="0" y1="5" x2="46" y2="5" stroke="#0b0b0b" stroke-width="1.3"/><path d="M45 1.5 L52 5 L45 8.5 Z" fill="#0b0b0b"/></svg>
    <span>finish</span>
  </div>

  <p class="blob-label label-efficiency">the way<br>to efficiency</p>
  <p class="blob-label label-matters">What<br>matters</p>
  <p class="blob-label label-takes">What it<br>takes</p>
  <p class="blob-label label-team">Benefiting<br>the entire<br>team</p>

  <p class="author">AUTHOR'S NAME</p>
</div>
</body>
</html>
```